The amber lantern with an elephant incorporated in the background

Target Market(s)

Real estate

Industry/Entity Type

Real Estate

Contact Information for Business Card

On back on want my name & number
In front I want the business name, "the amber lantern", below to say staging & design

Logo Text

The amber lantern

Font styles to use
Serif

Colors
000000

Requirements
Must have
• I want an elephant behind the writing in gold transperant

```html
<!DOCTYPE html>
<html lang="en">
<head>
<meta charset="utf-8">
<title>The Amber Lantern – Business Card</title>
<link rel="stylesheet" href="https://fonts.googleapis.com/css2?family=Open+Sans:wght@300;400&family=Oswald:wght@300&family=Allura&display=swap">
<style>
  :root {
    --backdrop: #6a4630;
    --card: #262626;
    --card-shade: #1d1d1d;
    --gold: #cfa94e;
    --gold-soft: #d9b865;
  }
  * { margin: 0; padding: 0; box-sizing: border-box; }
  html, body { width: 1200px; height: 1000px; overflow: hidden; }
  body { background: var(--backdrop); position: relative; }

  .card {
    position: absolute;
    left: 267px;
    width: 665px;
    height: 398px;
    background: var(--card);
    border-radius: 22px;
    overflow: hidden;
  }
  .card--front { top: 73px; }
  .card--back { top: 533px; }

  .card__mascot {
    position: absolute;
    left: 163px;
    top: 67px;
    width: 390px;
    height: 300px;
    background: var(--card-shade);
    border-radius: 40px;
  }

  .brand {
    position: absolute;
    left: 0;
    right: 0;
    top: 160px;
    text-align: center;
    color: var(--gold);
  }
  .brand__name {
    font-family: "Open Sans", sans-serif;
    font-weight: 400;
    font-size: 33px;
    letter-spacing: 3px;
    text-transform: uppercase;
    line-height: 1;
  }
  .brand__tagline {
    font-family: "Allura", cursive;
    font-size: 34px;
    line-height: 1;
    margin-top: 12px;
    padding-left: 14px;
  }

  .contact {
    position: absolute;
    left: 138px;
    top: 172px;
    display: flex;
    align-items: center;
    color: var(--gold);
  }
  .contact__name {
    font-family: "Oswald", sans-serif;
    font-weight: 300;
    font-size: 31px;
    letter-spacing: 1px;
    text-transform: uppercase;
    line-height: 1;
  }
  .contact__divider {
    width: 2px;
    height: 30px;
    background: var(--gold);
    margin: 0 24px;
  }
  .contact__details {
    font-family: "Open Sans", sans-serif;
    font-size: 15px;
    line-height: 22px;
    color: var(--gold-soft);
  }
</style>
</head>
<body>
  <section class="card card--front">
    <div class="card__mascot" role="img" aria-label="Faint dark elephant silhouette walking behind the name"></div>
    <div class="brand">
      <h1 class="brand__name">The Amber Lantern</h1>
      <p class="brand__tagline">staging &amp; design</p>
    </div>
  </section>

  <section class="card card--back">
    <div class="card__mascot" role="img" aria-label="Faint dark elephant silhouette walking behind the contact details"></div>
    <div class="contact">
      <p class="contact__name">Mara Ellison</p>
      <span class="contact__divider"></span>
      <div class="contact__details">
        <p>+ 000 000 0000</p>
        <p>info@theamberlantern.com</p>
      </div>
    </div>
  </section>
</body>
</html>
```